Brane & Hollis LLC
Commercial Real Estate Invesment Group
Brane & Hollis LLC -
Creative Brief
www.braneandhollisllc.example
Fitz & Co.focuses on Undervalued Assets that are cash flowing and have great potential upside.And the elimination of risk.
left side
www.quellmorefunds.example/#/home
www.ridgewaysyndicate.example
www.vantor.example
I need a lot of help here I am of no use visually at all. I do not even know how to answer most of the questions to you
dawnp dawnp
Guys that was the most painful and hard decision I have had to make in a very very long time. Thank you all you are all great and all of your effort was and is greatly appreciated. You are all genuineness and I am a lucky to have had you participate in this.
brightforge brightforge
Hello PH, Please check you PM inbox. Thanks
pixelmonk pixelmonk
Hi PH, Please check your private message. thanks,
Hey to everybody. This going to be a hard selection to be a hard selection process, Everything is great and Thank you for all of you work. I need to talk to support and ask a few questions, that I asked some privately and did not get answers to. I have kept this open because one particular designer asked me to, And I have this other Restaurant thing going on, that has stalled my attention to this. I spent some time doing some time eliminating some just to get a clearer view. I will have pick a winner by Sunday, Thank you all so much
Can Somebody put any thought on the Trelby Hall project please. I am opening that in 3 weeks.
Qv I really like this #29 can you go back to Who we are? Keep the arrow and maybe look for another building for the pic on the right. Fernwright #28 is ok but please re-read the brief and the thread we are a Commercial Real Estate Co.. Can I see it with maybe retail pics, strip centers? Please. Thank you
Lumo 24 & 26 are great 25 a little residential in feel. The path everybody is on is fantastic. A little more about us as a business, we have been investing in Commercial Real Estate as a group for 10 years after moving from Residential we primarily focusing on retail strip centers. We focus of Cash Flow and Dividends return in 1-2 years. And return on Capital by year 5 or sooner. We have a track record of of high returns and not losing money.
LuNaPix7Kw3Fo LuNaPix7Kw3Fo
Hello@dawnp, This is my 1st design hope you like it please feel free to let me know the required changes so that your expectations are met. waiting for your feedback on design#19, #20 & #21 Regrds, LunaPix
Vobe the lay out again is good. The modern building is not working. Thanks
We are US based. Thank you
Vobe4web Vobe4web
Which location are you look at? In US or UK, please advise me further..
And Oh it should be Brane & Hollis LLC is that not on the Logo? And can we try the lettering in the header in black?
I like the layout and concept. But the pic's are residential we need to be looking more retail-City scapeish. Thanks
SiteAdmin SiteAdmin
Logo files have been attached. Kindly see Creative Brief Owen Hartley
pelnoart pelnoart
can u upload your LOGO ?

```html
<!DOCTYPE html>
<html lang="en">
<head>
<meta charset="utf-8">
<title>Brane &amp; Hollis LLC — Who We Are</title>
<link rel="stylesheet" href="https://fonts.googleapis.com/css2?family=Arimo:ital,wght@0,400;0,700;1,400&family=Raleway:wght@200&display=swap">
<style>
  :root {
    --gold: #c9a14a;
    --gold-light: #ead7a6;
    --gold-pale: #f6eedb;
    --ink: #1d1d1d;
    --ink-soft: #555;
    --paper: #ffffff;
    --city-dusk: #5b6f93;
    --city-night: #2c2f3e;
    --glass-sky: #7fa6c9;
    --glass-deep: #2f5a78;
  }
  * { box-sizing: border-box; margin: 0; padding: 0; }
  html, body { width: 1200px; height: 871px; overflow: hidden; background: var(--paper); }
  body { font-family: "Arimo", Arial, sans-serif; color: var(--ink); position: relative; }

  .page-frame {
    position: absolute; inset: 0;
    border: 4px solid var(--gold-light);
    outline: 1px solid var(--gold);
    outline-offset: -5px;
  }

  .account-links {
    position: absolute; top: 31px; right: 40px;
    font-size: 14px; color: var(--ink-soft);
  }
  .account-links span { margin: 0 6px; }

  .sidebar {
    position: absolute; left: 48px; top: 67px; width: 284px; height: 744px;
    border: 4px solid var(--gold);
    background: var(--paper);
  }
  .brand {
    position: absolute; left: 18px; top: 22px; right: 14px;
    display: flex; align-items: center; gap: 10px;
    padding-bottom: 14px; border-bottom: 2px solid var(--gold);
  }
  .brand-square { width: 34px; height: 34px; background: var(--gold); flex: none; }
  .brand-name { font-size: 22px; font-weight: 700; color: var(--ink); white-space: nowrap; }

  .nav { position: absolute; right: 10px; text-align: right; list-style: none; }
  .nav li { font-size: 18px; line-height: 25px; text-transform: uppercase; color: var(--ink); }
  .nav-main { top: 106px; }
  .nav-secondary { top: 296px; }

  .sidebar-decor {
    position: absolute; left: 0; right: 0; bottom: 0; height: 330px;
    background: linear-gradient(180deg, var(--paper) 0%, var(--gold-pale) 45%, var(--gold-light) 100%);
  }

  .hero-photo {
    position: absolute; left: 367px; top: 89px; width: 538px; height: 311px;
    background: linear-gradient(180deg, var(--city-dusk) 0%, #8b7f93 45%, var(--city-night) 100%);
  }
  .page-title {
    position: absolute; left: 367px; top: 333px;
    font-family: "Raleway", "Helvetica Neue", sans-serif; font-weight: 200;
    font-size: 72px; line-height: 72px; letter-spacing: 1px;
    color: var(--paper);
    white-space: nowrap;
  }
  .side-photo {
    position: absolute; left: 914px; top: 89px; width: 243px; height: 311px;
    background: linear-gradient(160deg, var(--glass-sky) 0%, #4f7fa3 50%, var(--glass-deep) 85%, #4d7a3a 100%);
  }

  .intro {
    position: absolute; left: 367px; top: 425px; width: 495px;
    font-size: 15.6px; line-height: 25px; color: var(--ink);
  }

  .pull-quote {
    position: absolute; left: 925px; top: 430px; width: 235px;
    font-size: 28px; line-height: 34px; color: var(--ink);
  }
  .pull-quote cite {
    display: block; text-align: right; margin-top: 18px; padding-right: 8px;
    font-style: italic; font-size: 24px;
  }

  .footer {
    position: absolute; right: 40px; top: 820px;
    font-size: 11.5px; color: var(--ink-soft);
    display: flex; gap: 14px;
  }
  .footer .divider { margin: 0 -6px; }
</style>
</head>
<body>
  <div class="page-frame"></div>

  <div class="account-links">Sign In<span>|</span>Register</div>

  <aside class="sidebar">
    <div class="brand">
      <span class="brand-square"></span>
      <span class="brand-name">Brane &amp; Hollis LLC</span>
    </div>
    <ul class="nav nav-main">
      <li>Home</li>
      <li>Our Approach</li>
      <li>Who We Are</li>
      <li>What We Invest In</li>
      <li>People</li>
      <li>Contact Us</li>
    </ul>
    <ul class="nav nav-secondary">
      <li>News</li>
      <li>Announcements</li>
      <li>Investing</li>
    </ul>
    <div class="sidebar-decor" role="img" aria-label="Faint gold outline of commercial buildings"></div>
  </aside>

  <div class="hero-photo" role="img" aria-label="City skyline at dusk with a tall glass office tower"></div>
  <h1 class="page-title">WHO WE ARE</h1>
  <div class="side-photo" role="img" aria-label="Glass commercial tower against a blue sky"></div>

  <p class="intro">Lorem ipsum dolor sit amet, consectetur adipiscing elit. Nullam lorem justo, volutpat vitae aliquet eget, rutrum id ante. Nam vestibulum sapien ac felis interdum aliquam eu luctus ipsum. Nam sollicitudin feugiat tristique. Maecenas sit amet velit urna, at lacinia magna. Nam volutpat nisl libero. Cras non justo lacus, id blandit quam. Nunc ac lacus nibh, et lobortis ante. Pellentesque eget magna ac lectus ultrices semper in et tortor. Phasellus a consequat nulla. Integer tempus molestie lorem sed tristique. Integer vel est ante, nec mattis magna. Maecenas euismod mauris mauris, in porta tellus. Maecenas vulputate tincidunt eros.</p>

  <blockquote class="pull-quote">
    &ldquo;Lorem ipsum dolor sit amet, consectetur ad-ipiscing elit. Nullam.&rdquo;
    <cite>-Lorem Ipsum</cite>
  </blockquote>

  <footer class="footer">
    <span>Copyright 2011</span><span class="divider">|</span>
    <span>New York</span><span>Press Room</span><span>Charities</span>
    <span>Portfolio</span><span>Site Map</span><span>Legal</span>
  </footer>
</body>
</html>
```